Debut book club fiction author needs a book cover design

I need a book cover design (and a separate e-book thumbnail also) for my book club/women's fiction debut that I am launching on Brightleaf Press Portal. I've included the brief/back cover blurb as below to give you a flavour of the book. I'm after something striking but simple, maybe with a wine glass lurking in the background and/or an abandoned dummy/pacifier or empty crib?? I've attached a few competitor style covers that i like for reference.

Target Market(s)

Women's fiction readers

Industry/Entity Type

Women's fiction/publishing

Font styles to use
Serif

Requirements
Must have
• Title: Every Quiet Hour. Name: Maren Tolley. The full 'pitch/blurb' on the back cover which I've included as a file below named 'pitch'
Nice to have
• Open to suggestions, but an image which reflects the struggle captured in the book in a bold simple image

```html
<!DOCTYPE html>
<html lang="en">
<head>
<meta charset="utf-8">
<title>Every Quiet Hour — Book Cover Wrap</title>
<link rel="stylesheet" href="https://fonts.googleapis.com/css2?family=Jost:wght@400;500;600&family=Cormorant+Garamond:ital,wght@1,400;1,500&display=swap">
<style>
  :root {
    --page-bg: #efefef;
    --cover-black: #000000;
    --spine-black: #080808;
    --ink-white: #ffffff;
    --accent-blue: #3ea3ec;
    --accent-orange: #ec7412;
    --glow-orange: #b55510;
    --glow-deep: #2a1206;
  }
  * { margin: 0; padding: 0; box-sizing: border-box; }
  html, body {
    width: 1200px; height: 1200px; overflow: hidden;
    background: var(--page-bg);
  }
  .book-wrap {
    position: absolute; left: 50px; top: 210px;
    width: 1100px; height: 780px;
    display: flex;
  }

  /* Back cover */
  .back-cover {
    width: 520px; height: 780px;
    background: var(--cover-black);
    color: var(--ink-white);
    padding: 88px 52px 0;
    font-family: "Jost", sans-serif;
  }
  .back-title {
    text-align: center;
    font-size: 30px; font-weight: 500;
    letter-spacing: 3px;
    margin-bottom: 22px;
  }
  .back-title .title-italic {
    font-family: "Cormorant Garamond", serif;
    font-style: italic; font-weight: 400;
    font-size: 32px; letter-spacing: 1px;
    text-transform: none;
  }
  .back-tagline {
    text-align: center;
    font-style: italic; font-size: 14px;
    margin-bottom: 24px;
  }
  .blurb p {
    font-size: 13.2px; line-height: 1.62;
    text-align: justify; text-align-last: center;
    margin-bottom: 20px;
  }

  /* Spine */
  .spine {
    width: 60px; height: 780px;
    background: var(--spine-black);
    border-left: 1px solid #1c1c1c;
    border-right: 1px solid #1c1c1c;
    display: flex; flex-direction: column; align-items: center;
    padding: 36px 0 30px;
    writing-mode: vertical-rl;
    font-family: "Jost", sans-serif;
  }
  .spine-title {
    color: var(--ink-white);
    font-size: 19px; font-weight: 500; letter-spacing: 4px;
    white-space: nowrap;
  }
  .spine-title .title-italic {
    font-family: "Cormorant Garamond", serif;
    font-style: italic; font-weight: 400; letter-spacing: 2px;
  }
  .spine-tagline {
    color: var(--accent-blue);
    font-size: 9px; letter-spacing: 2px; line-height: 1.3;
    margin-top: 46px; white-space: nowrap;
  }
  .spine-author {
    color: var(--accent-orange);
    font-size: 15px; font-weight: 500; letter-spacing: 4px;
    margin-top: auto; white-space: nowrap;
  }

  /* Front cover */
  .front-cover {
    position: relative;
    width: 520px; height: 780px;
    background: var(--cover-black);
    overflow: hidden;
    font-family: "Jost", sans-serif;
    color: var(--ink-white);
    text-align: center;
  }
  .cover-art { position: absolute; inset: 0; }
  .front-text { position: relative; z-index: 1; }
  .front-tagline {
    color: var(--accent-blue);
    font-size: 24px; font-weight: 500; letter-spacing: 2px;
  }
  .front-tagline.line-one { padding-top: 60px; }
  .front-title-word {
    font-weight: 500; line-height: 0.9; letter-spacing: 2px;
  }
  .word-every { font-size: 138px; margin-top: 8px; }
  .front-tagline.line-two { margin-top: 18px; }
  .word-quiet {
    font-family: "Cormorant Garamond", serif;
    font-style: italic; font-weight: 400;
    font-size: 96px; letter-spacing: 6px;
    margin-top: 48px; line-height: 1;
  }
  .word-hour { font-size: 168px; margin-top: 40px; }
  .front-author {
    color: var(--accent-orange);
    font-size: 50px; font-weight: 500; letter-spacing: 5px;
    margin-top: 42px;
  }
</style>
</head>
<body>
  <div class="book-wrap">
    <section class="back-cover">
      <h2 class="back-title">EVERY <span class="title-italic">Quiet</span> HOUR</h2>
      <p class="back-tagline">‘All the women wanted was a child of their own…’</p>
      <div class="blurb">
        <p>Reception teacher, Lana, and partner and part-time DJ Joel can’t afford private IVF treatment. Equally they can’t afford not to. Lana’s mental health is deteriorating as she longs for the child that has eluded her to date.</p>
        <p>In her 37 years Tilda Asquith-Hyde has never felt maternal. However, following the breakdown of her long-term relationship, and mother’s death she finds herself in receipt of an eye-watering inheritance. No longer needing to work she becomes increasingly isolated and even alcohol, her only constant, no longer fills the void. After a chance encounter with an old friend and her baby, Tilda seizes upon the idea that motherhood will be the missing piece in her lonely life.</p>
        <p>Both parties access IVF treatment at the same clinic, Tilda opting for a sperm donor and Lana and Joel using their own fertilised egg.</p>
        <p>But within moments of giving birth, Tilda is convinced that the child in her arms is not biologically hers, setting off a devastating chain of events. How far will both women go to ‘do the right thing’ for their children? It’s enough to drive anyone to drink. Isn’t it?</p>
      </div>
    </section>

    <aside class="spine">
      <span class="spine-title">EVERY <span class="title-italic">Quiet</span> HOUR</span>
      <span class="spine-tagline">All the women wanted was a<br>child of their own…</span>
      <span class="spine-author">MAREN TOLLEY</span>
    </aside>

    <section class="front-cover">
      <svg class="cover-art" width="520" height="780" viewBox="0 0 520 780" role="img" aria-label="Empty rocking cradle draped with a blue blanket, standing on a dark wooden floor lit by a warm orange glow">
        <defs>
          <radialGradient id="floorGlow" cx="0.58" cy="0.74" r="0.62">
            <stop offset="0" stop-color="var(--glow-orange)"/>
            <stop offset="0.35" stop-color="#5a2a0c"/>
            <stop offset="0.7" stop-color="var(--glow-deep)"/>
            <stop offset="1" stop-color="#000000"/>
          </radialGradient>
          <radialGradient id="cradleTone" cx="0.5" cy="0.5" r="0.5">
            <stop offset="0" stop-color="#1f5f9c" stop-opacity="0.75"/>
            <stop offset="1" stop-color="#0a1a2c" stop-opacity="0"/>
          </radialGradient>
        </defs>
        <rect width="520" height="780" fill="url(#floorGlow)"/>
        <ellipse cx="300" cy="420" rx="130" ry="150" fill="url(#cradleTone)"/>
      </svg>
      <div class="front-text">
        <p class="front-tagline line-one">All the women wanted was a</p>
        <h1 class="front-title-word word-every">EVERY</h1>
        <p class="front-tagline line-two">child of their own…</p>
        <p class="word-quiet">Quiet</p>
        <p class="front-title-word word-hour">HOUR</p>
        <p class="front-author">MAREN TOLLEY</p>
      </div>
    </section>
  </div>
</body>
</html>
```